Medical equipment business looking for professional, unique business card

We need a business card design for a durable medical equipment company. We are small but would like our cards to express that we are much bigger. We focus on braces (back, knee, wrist, etc) but also do crutches, rollators, wheelchairs- basically medical equipment that gets you going and back in Action. Our colors are blue and green and our logo has an arrow and use of a "spine". We'd like to express professionalism while being unique.

Industry/Entity Type

Medical Equipment

Contact Information for Business Card

Professional feel but unique. Memorable.

Font styles to use
Serif
Sans Serif
Other font styles liked:
• verdana

Requirements
Must have
• card holders cell#, business phone#, fax#, email, website address, business address, logo
Nice to have
• use of medical/healthcare related descriptive words, items, look
Should not have
• the wrong colors or cartoon characters.

```html
<!DOCTYPE html>
<html lang="en">
<head>
<meta charset="utf-8">
<title>Motiva Medical – Business Card</title>
<link href="https://fonts.googleapis.com/css2?family=Arimo:wght@400;700&display=swap" rel="stylesheet">
<style>
  :root {
    --backdrop: #2a2a2c;
    --navy: #0d4a7c;
    --navy-deep: #083a66;
    --navy-light: #1565a0;
    --green: #6cc43a;
    --sky: #1aa0d8;
    --white: #ffffff;
    --paper: #f2f2f2;
    --ink: #0d4a7c;
  }
  * { box-sizing: border-box; margin: 0; padding: 0; }
  html, body { width: 1200px; height: 800px; overflow: hidden; }
  body {
    background: var(--backdrop);
    font-family: "Arimo", Arial, sans-serif;
    display: flex;
    flex-direction: column;
    align-items: center;
    justify-content: center;
    gap: 44px;
  }
  .card {
    position: relative;
    width: 600px;
    height: 340px;
    border-radius: 14px;
    overflow: hidden;
  }
  .card-bg { position: absolute; inset: 0; width: 100%; height: 100%; }

  /* Front */
  .card--front { background: var(--paper); }
  .brand {
    position: absolute;
    display: flex;
    flex-direction: column;
    align-items: flex-start;
  }
  .brand-row { display: flex; align-items: center; gap: 10px; }
  .brand-dot { width: 14px; height: 14px; border-radius: 50%; background: var(--green); }
  .brand-name { font-weight: 700; letter-spacing: -0.5px; line-height: 1; }
  .brand-tagline { font-weight: 700; color: var(--sky); }

  .card--front .brand { left: 170px; top: 60px; }
  .card--front .brand-name { font-size: 44px; color: var(--ink); }
  .card--front .brand-tagline { font-size: 15px; margin: 8px 0 0 24px; }

  .holder {
    position: absolute;
    left: 0;
    bottom: 0;
    width: 100%;
    height: 120px;
    display: flex;
    align-items: center;
    padding: 18px 24px 0 40px;
    color: var(--white);
  }
  .holder-id { text-align: right; padding-right: 16px; border-right: 1px solid rgba(255,255,255,.35); }
  .holder-name { font-size: 21px; font-weight: 700; letter-spacing: .3px; }
  .holder-title { font-size: 15px; margin-top: 3px; }
  .holder-contact { padding-left: 16px; font-size: 14px; line-height: 1.4; }
  .label { color: var(--green); font-weight: 700; }
  .accent { color: var(--green); }

  /* Back */
  .card--back { background: linear-gradient(135deg, var(--navy-light) 0%, var(--navy) 55%, var(--navy-deep) 100%); }
  .card--back .brand { left: 50%; top: 50%; transform: translate(-50%, -50%); }
  .card--back .brand-name { font-size: 52px; color: var(--white); }
  .card--back .brand-tagline { font-size: 17px; margin: 10px 0 0 26px; }
</style>
</head>
<body>

  <section class="card card--front" aria-label="Business card front">
    <svg class="card-bg" viewBox="0 0 600 340" preserveAspectRatio="none" aria-hidden="true">
      <defs>
        <linearGradient id="frontBlue" x1="0" y1="0" x2="1" y2="1">
          <stop offset="0" stop-color="#1565a0"/>
          <stop offset="1" stop-color="#083a66"/>
        </linearGradient>
      </defs>
      <path d="M0 240 C 170 205, 380 180, 600 180 L600 340 L0 340 Z" fill="url(#frontBlue)"/>
      <path d="M0 220 C 170 190, 360 172, 530 168 L530 178 C 360 182, 170 200, 0 240 Z" fill="var(--green)"/>
      <path d="M524 158 L560 172 L524 184 Z" fill="var(--green)"/>
    </svg>

    <div class="brand">
      <div class="brand-row">
        <span class="brand-dot"></span>
        <span class="brand-name">Motiva Medical</span>
      </div>
      <span class="brand-tagline">Durable Medical Equipment</span>
    </div>

    <div class="holder">
      <div class="holder-id">
        <p class="holder-name">JORDAN PIERCE</p>
        <p class="holder-title">General Manager</p>
      </div>
      <div class="holder-contact">
        <p>48 Harbor St, Suite 305, Lakeview MA 02100</p>
        <p><span class="label">M:</span> 555-014-2387 · <span class="label">T:</span> 555-019-6630</p>
        <p><span class="label">E:</span> hello@MotivaMed.com · www.<span class="accent">MotivaMed</span>.com</p>
      </div>
    </div>
  </section>

  <section class="card card--back" aria-label="Business card back">
    <div class="brand">
      <div class="brand-row">
        <span class="brand-dot"></span>
        <span class="brand-name">Motiva Medical</span>
      </div>
      <span class="brand-tagline">Durable Medical Equipment</span>
    </div>
  </section>

</body>
</html>
```